KVOB Presentation (Meridian Study & Learning Academy)

We need a befitting corporate presentation for an international institute affiliated to a multilateral development bank based in Jeddah, Saudi Arabia. The institute primarily provides research, capacity development, knowledge-based solutions, and publications in Islamic Economics, Banking & Finance. Our services target mainly banking and financial institutions, regulatory authorities, other multi-laterals, academic institutions, and other institutions and personnel involved with development activities. The corporate presentation should reflect our vision and rich historical past. We have attached here a draft of the presentation. We need it beautifully re-designed with lots of graphics and animations. If any additional information is required, please contact us.
Updates

Please note that final project must be provided to us in PowerPoint Presentation format. Thank you.

Colors

Designer to choose colors to be used in the design.

Requirements
Must have
• Final project must be submitted to us in PowerPoint Presentation (.ppt) format.
Nice to have
• Suitable clip art images in slides containing lists or itemized content.

```html
<!DOCTYPE html>
<html lang="en">
<head>
<meta charset="utf-8">
<title>KVOB Presentation — Meridian Study &amp; Learning Academy</title>
<link rel="stylesheet" href="https://fonts.googleapis.com/css2?family=Open+Sans:wght@400;600;700&family=Montserrat:wght@600;700&display=swap">
<style>
:root{
  --bg:#ffffff;
  --green:#1fa64a;
  --green-dark:#0f6b34;
  --green-light:#3cc46a;
  --gold:#8a7a3c;
  --gold-light:#b59f55;
  --cream:#f4efe0;
  --ink:#333333;
  --muted:#777777;
  --dark:#2a2c30;
  --frame:#d4d4d4;
}
*{box-sizing:border-box;margin:0;padding:0}
html,body{width:1200px;height:551px;overflow:hidden;background:var(--bg);font-family:"Open Sans",Arial,sans-serif;color:var(--ink)}
.sorter{position:relative;width:1200px;height:551px}
.thumb{position:absolute;width:173px}
.slide{position:relative;width:173px;height:98px;overflow:hidden;border:1px solid var(--frame);background:#fff}
.meta{display:flex;justify-content:space-between;font-size:11px;color:#444;padding:2px 1px 0 1px}
.meta .star{color:#666;font-size:9px}
.light{background:linear-gradient(180deg,var(--cream) 0,#fff 22px)}
.title{position:absolute;left:8px;top:5px;font-size:6.5px;color:var(--green);font-weight:600}
.dark .title{color:#fff}
.abs{position:absolute}
.tiny{font-size:3.2px;line-height:1.35;color:var(--ink)}
.foot-badge{position:absolute;right:5px;bottom:4px;width:8px;height:8px;border-radius:2px;background:var(--green)}
.photo{position:absolute}
.section-box{position:absolute;left:18px;top:38px;width:78px;height:27px;background:#fff;display:flex;align-items:center;justify-content:center;text-align:center;font-family:Montserrat,Arial,sans-serif;font-weight:700;font-size:7px;line-height:1.05;color:#5c5c5c;transform:skewX(-4deg)}
.tile{position:absolute;background:rgba(138,122,60,.92);color:#fff;font-size:3px;font-weight:600;padding:2px;line-height:1.3;border-radius:1px}
.pill{position:absolute;height:8px;border:1px solid var(--gold-light);border-radius:5px;font-size:3px;font-weight:700;display:flex;align-items:center;justify-content:center;color:var(--ink);background:#fff}
</style>
</head>
<body>
<main class="sorter">

<!-- 1 Cover -->
<section class="thumb" style="left:14px;top:10px">
  <div class="slide">
    <div class="photo" role="img" aria-label="Faded city skyline photograph" style="left:60px;top:0;width:113px;height:98px;background:linear-gradient(90deg,#fff,#e4e4e2 50%,#d2d2cf)"></div>
    <svg class="abs" style="left:0;top:0" width="60" height="98"><rect x="14" width="4" height="98" fill="#1fa64a"/><rect x="20" width="2" height="98" fill="#3cc46a"/><rect x="24" width="5" height="98" fill="#cfe9d6"/></svg>
    <div class="abs" style="left:48px;top:10px;width:9px;height:9px;border-radius:50%;background:var(--green)"></div>
    <div class="abs" style="left:36px;top:22px;font-size:4px;color:var(--green-dark);font-weight:700">KVOB</div>
    <div class="abs" style="left:36px;top:46px;font-size:4.6px;color:var(--green);font-weight:600;line-height:1.25;width:70px">MERIDIAN STUDY &amp; LEARNING ACADEMY<br>( KVOB )</div>
    <div class="abs tiny" style="left:36px;top:66px;color:var(--muted)">www.kvob.org</div>
    <div class="abs" style="left:36px;top:84px;width:6px;height:6px;border-radius:50%;background:var(--green)"></div>
    <div class="abs tiny" style="left:44px;top:84px;color:var(--muted)">Member of the<br>Northgate Development Bank Group</div>
  </div>
  <div class="meta"><span>1</span><span class="star">★</span></div>
</section>

<!-- 2 Group -->
<section class="thumb" style="left:214px;top:10px">
  <div class="slide light">
    <div class="title">NDB group</div>
    <div class="abs tiny" style="left:8px;top:22px;width:40px;color:var(--muted)">Meridian Study and Learning Academy</div>
    <div class="abs tiny" style="left:8px;top:46px;width:40px;color:var(--muted)">Corporation for Export Credit Cover</div>
    <div class="abs tiny" style="left:8px;top:70px;width:40px;color:var(--muted)">Private Sector Development Corporation</div>
    <div class="abs tiny" style="left:112px;top:22px;width:45px;color:var(--muted)">International Trade Finance Fund</div>
    <div class="abs tiny" style="left:112px;top:70px;width:45px;color:var(--muted)">Solidarity Fund for Development</div>
    <svg class="abs" style="left:50px;top:14px" width="70" height="78">
      <circle cx="35" cy="39" r="24" fill="none" stroke="#e2dcc5" stroke-width="4"/>
      <circle cx="35" cy="39" r="13" fill="#fff" stroke="#b59f55" stroke-width="1"/>
      <circle cx="15" cy="14" r="6" fill="#fff" stroke="#1fa64a" stroke-width="1.5"/>
      <circle cx="55" cy="14" r="6" fill="#fff" stroke="#1fa64a" stroke-width="1.5"/>
      <circle cx="11" cy="39" r="6" fill="#fff" stroke="#1fa64a" stroke-width="1.5"/>
      <circle cx="15" cy="64" r="6" fill="#fff" stroke="#1fa64a" stroke-width="1.5"/>
      <circle cx="55" cy="64" r="6" fill="#fff" stroke="#1fa64a" stroke-width="1.5"/>
      <text x="35" y="41" font-size="5" font-weight="700" fill="#0f6b34" text-anchor="middle" font-family="Open Sans,sans-serif">NDB</text>
    </svg>
    <div class="abs" style="left:97px;top:48px;font-size:3.6px;color:#c9bf9a;font-weight:700;line-height:1.2">NORTHGATE<br>DEVELOPMENT<br>BANK GROUP</div>
    <div class="foot-badge"></div>
  </div>
  <div class="meta"><span>2</span><span class="star">★</span></div>
</section>

<!-- 3 Milestones -->
<section class="thumb" style="left:414px;top:10px">
  <div class="slide light">
    <div class="title">KVOB milestones</div>
    <svg class="abs" style="left:0;top:0" width="173" height="98">
      <path d="M4 60 Q14 52 24 60 T44 60 T64 60 T84 60 T104 60 T124 60 T144 60 T164 60" fill="none" stroke="#1fa64a" stroke-width="2"/>
      <g fill="#1fa64a"><circle cx="14" cy="56" r="3"/><circle cx="30" cy="62" r="3"/><circle cx="46" cy="56" r="3"/><circle cx="62" cy="62" r="3"/><circle cx="78" cy="56" r="3"/><circle cx="94" cy="62" r="3"/><circle cx="110" cy="56" r="3"/><circle cx="126" cy="62" r="3"/><circle cx="142" cy="56" r="3"/></g>
      <path d="M160 54 l6 6 -6 6" fill="none" stroke="#1fa64a" stroke-width="2"/>
    </svg>
    <div class="abs tiny" style="left:8px;top:38px">Founded</div>
    <div class="abs tiny" style="left:38px;top:34px;width:20px">Launched group prize</div>
    <div class="abs tiny" style="left:70px;top:30px;width:20px">Launched regional network</div>
    <div class="abs tiny" style="left:102px;top:34px;width:20px">Launched KVOB research</div>
    <div class="abs tiny" style="left:134px;top:30px;width:24px">Launched global leadership programme</div>
    <div class="abs tiny" style="left:22px;top:70px">Operational</div>
    <div class="abs tiny" style="left:54px;top:70px;width:20px">Became group entity</div>
    <div class="abs tiny" style="left:86px;top:70px;width:20px">Launched distance learning</div>
    <div class="abs tiny" style="left:118px;top:70px;width:20px">Launched KVOB workshops</div>
    <div class="foot-badge"></div>
  </div>
  <div class="meta"><span>3</span><span class="star">★</span></div>
</section>

<!-- 4 Section: Innovative Research -->
<section class="thumb" style="left:614px;top:10px">
  <div class="slide" style="border:2px solid #666">
    <div class="photo" role="img" aria-label="Photograph of glass office towers against a blue sky" style="left:70px;top:0;width:103px;height:98px;background:linear-gradient(160deg,#0d4e86,#5f9fd3 55%,#cfe2f2);clip-path:polygon(25% 0,100% 0,100% 100%,0 100%)"></div>
    <svg class="abs" style="left:0;top:0" width="173" height="98"><polygon points="0,0 95,0 75,98 0,98" fill="#1fa64a"/><polygon points="0,98 40,60 60,98" fill="#0f6b34"/><polygon points="30,10 38,3 42,13" fill="#0f6b34"/></svg>
    <div class="section-box">INNOVATIVE<br>RESEARCH</div>
  </div>
  <div class="meta"><span>4</span><span class="star">★</span></div>
</section>

<!-- 5 About KVOB section -->
<section class="thumb" style="left:814px;top:10px">
  <div class="slide">
    <div class="photo" role="img" aria-label="Photograph of glass office towers" style="left:60px;top:0;width:113px;height:98px;background:linear-gradient(160deg,#0d4e86,#5f9fd3 55%,#cfe2f2)"></div>
    <svg class="abs" style="left:0;top:0" width="173" height="98"><polygon points="0,0 105,0 80,98 0,98" fill="#1fa64a"/><polygon points="105,0 120,0 95,98 80,98" fill="#3cc46a" opacity=".6"/></svg>
    <div class="abs" style="left:8px;top:40px;font-family:Montserrat,sans-serif;font-weight:700;font-size:10px;color:#fff;line-height:1.1">ABOUT<br>KVOB</div>
    <div class="foot-badge" style="background:#fff"></div>
  </div>
  <div class="meta"><span>5</span><span class="star">★</span></div>
</section>

<!-- 6 About -->
<section class="thumb" style="left:1014px;top:10px">
  <div class="slide light">
    <div class="title">About KVOB</div>
    <div class="abs tiny" style="left:8px;top:20px;width:98px">• Meridian Study and Learning Academy leads knowledge creation and sharing in economics, banking and finance for member countries.<br><br>• We lead in providing innovative knowledge-based solutions to development challenges in member countries.<br><br>• We lead in providing training and capacity building aligned with sustainable development goals.<br><br>• A global leader whose partners and networks support the development of a fair financial industry.</div>
    <svg class="abs" style="left:112px;top:18px" width="58" height="78" fill="none" stroke="#c9bf9a" stroke-width=".6">
      <path d="M6 70 Q30 50 30 30 T54 6"/>
      <g fill="#c9bf9a"><circle cx="30" cy="10" r="3"/><circle cx="44" cy="18" r="3"/><circle cx="20" cy="26" r="3"/><circle cx="38" cy="34" r="3"/><circle cx="50" cy="42" r="3"/><circle cx="28" cy="48" r="3"/><circle cx="14" cy="58" r="3"/><circle cx="40" cy="62" r="3"/><circle cx="24" cy="72" r="3"/></g>
    </svg>
  </div>
  <div class="meta"><span>6</span><span class="star">★</span></div>
</section>

<!-- 7 KVOB in numbers bars -->
<section class="thumb" style="left:14px;top:149px">
  <div class="slide light">
    <div class="title">KVOB in numbers</div>
    <svg class="abs" style="left:8px;top:19px" width="120" height="76" font-family="Open Sans,sans-serif">
      <g fill="#1fa64a">
        <rect x="0" y="0" width="90" height="5" rx="2.5"/><rect x="0" y="9" width="64" height="5" rx="2.5"/><rect x="0" y="18" width="44" height="5" rx="2.5"/><rect x="0" y="27" width="44" height="5" rx="2.5"/><rect x="0" y="36" width="36" height="5" rx="2.5"/><rect x="0" y="45" width="28" height="5" rx="2.5"/><rect x="0" y="54" width="20" height="5" rx="2.5"/><rect x="0" y="63" width="20" height="5" rx="2.5"/>
      </g>
      <g fill="#1fa64a" font-size="5" font-weight="700"><text x="93" y="5">14</text><text x="67" y="14">9</text><text x="47" y="23">5</text><text x="47" y="32">5</text><text x="39" y="41">4</text><text x="31" y="50">3</text><text x="23" y="59">2</text><text x="23" y="68">2</text></g>
      <g fill="#777" font-size="2.8"><text x="101" y="5">Admin specialists</text><text x="72" y="14">Researchers</text><text x="52" y="23">Publication Specialists</text><text x="52" y="32">Training Specialists</text><text x="44" y="41">Management</text><text x="36" y="50">Finance Specialists</text><text x="28" y="59">Technology Specialists</text><text x="28" y="68">Financial Analysts</text></g>
    </svg>
    <div class="foot-badge"></div>
  </div>
  <div class="meta"><span>7</span><span class="star">★</span></div>
</section>

<!-- 8 KVOB in numbers dark -->
<section class="thumb" style="left:214px;top:149px">
  <div class="slide dark" role="img" aria-label="Dark photograph of a digital network background" style="background:radial-gradient(circle at 60% 40%,#5a5b5e,#202125)">
    <div class="title">KVOB in numbers</div>
    <svg class="abs" style="left:0;top:22px" width="173" height="30">
      <line x1="6" y1="8" x2="167" y2="8" stroke="#fff" stroke-width=".6"/>
      <g fill="#fff" stroke="#1fa64a" stroke-width="1.5"><circle cx="14" cy="8" r="6"/><circle cx="34" cy="8" r="6"/><circle cx="54" cy="8" r="6"/><circle cx="74" cy="8" r="6"/><circle cx="94" cy="8" r="6"/><circle cx="114" cy="8" r="6"/><circle cx="134" cy="8" r="6"/><circle cx="154" cy="8" r="6"/></g>
      <g stroke="#fff" stroke-width=".5"><line x1="14" y1="14" x2="14" y2="30"/><line x1="34" y1="14" x2="34" y2="30"/><line x1="54" y1="14" x2="54" y2="30"/><line x1="74" y1="14" x2="74" y2="30"/><line x1="94" y1="14" x2="94" y2="30"/><line x1="114" y1="14" x2="114" y2="30"/><line x1="134" y1="14" x2="134" y2="30"/><line x1="154" y1="14" x2="154" y2="30"/></g>
    </svg>
    <div class="abs" style="left:0;top:52px;width:173px;height:22px;background:rgba(138,122,60,.92)"></div>
    <svg class="abs" style="left:0;top:54px" width="173" height="20" font-family="Open Sans,sans-serif" text-anchor="middle" fill="#fff">
      <g font-size="6" font-weight="700"><text x="14" y="8">14</text><text x="34" y="8">9</text><text x="54" y="8">5</text><text x="74" y="8">5</text><text x="94" y="8">4</text><text x="114" y="8">3</text><text x="134" y="8">2</text><text x="154" y="8">2</text></g>
      <g font-size="2.6"><text x="14" y="13">admin</text><text x="34" y="13">Researchers</text><text x="54" y="13">Publication</text><text x="74" y="13">Training</text><text x="94" y="13">Management</text><text x="114" y="13">Finance</text><text x="134" y="13">Technology</text><text x="154" y="13">Analysts</text></g>
    </svg>
  </div>
  <div class="meta"><span>8</span><span class="star">★</span></div>
</section>

<!-- 9 KVOB in numbers donut -->
<section class="thumb" style="left:414px;top:149px">
  <div class="slide light">
    <div class="title">KVOB in numbers (1981-2019)</div>
    <svg class="abs" style="left:0;top:0" width="173" height="98" font-family="Open Sans,sans-serif">
      <g fill="none" stroke-width="12">
        <circle cx="60" cy="58" r="26" stroke="#8a7a3c" stroke-dasharray="26 4.8"/>
      </g>
      <circle cx="60" cy="58" r="14" fill="#fff"/>
      <g fill="#fff" font-size="4.5" font-weight="700" text-anchor="middle"><text x="60" y="35">377</text><text x="83" y="47">23</text><text x="83" y="73">63</text><text x="60" y="86">19</text><text x="37" y="73">729</text><text x="37" y="47">405</text></g>
      <text x="60" y="59" font-size="2.6" fill="#777" text-anchor="middle">1981 - 2019</text>
      <polygon points="96,18 118,18 118,12 128,24 118,36 118,30 96,30" fill="#1fa64a"/>
      <g fill="#fff"><rect x="104" y="21" width="3" height="6"/><rect x="109" y="21" width="3" height="6"/><rect x="114" y="21" width="3" height="6"/></g>
      <g fill="#555" font-size="2.8"><text x="28" y="26">Research Projects</text><text x="88" y="28">Publications</text><text x="10" y="45">Conferences</text><text x="98" y="50">Knowledge</text><text x="98" y="53.5">Dissemination</text><text x="98" y="73">Reassignment</text><text x="10" y="70">Training</text><text x="10" y="73.5">Programs</text><text x="10" y="92">Online learning Programs</text><text x="72" y="92">Advisory Projects</text></g>
    </svg>
    <div class="foot-badge"></div>
  </div>
  <div class="meta"><span>9</span><span class="star">★</span></div>
</section>

<!-- 10 What we do -->
<section class="thumb" style="left:614px;top:149px">
  <div class="slide light">
    <div class="title">What we do</div>
    <svg class="abs" style="left:0;top:0" width="173" height="98">
      <g fill="none" stroke="#999" stroke-width=".5" stroke-dasharray="1.5 1"><path d="M56 30 Q76 30 76 46"/><path d="M118 30 Q98 30 98 46"/><path d="M56 76 Q76 76 76 62"/><path d="M118 76 Q98 76 98 62"/></g>
      <g fill="#c9bf9a"><polygon points="22,36 34,36 28,42"/><polygon points="138,36 150,36 144,42"/><polygon points="22,70 34,70 28,64"/><polygon points="138,70 150,70 144,64"/></g>
      <circle cx="87" cy="54" r="13" fill="#1fa64a" stroke="#cfe9d6" stroke-width="2"/>
      <text x="87" y="53" font-size="3.6" fill="#fff" font-weight="700" text-anchor="middle" font-family="Open Sans,sans-serif">KVOB</text>
      <text x="87" y="58" font-size="3.6" fill="#fff" font-weight="700" text-anchor="middle" font-family="Open Sans,sans-serif">ACTIVITIES</text>
    </svg>
    <div class="pill" style="left:8px;top:26px;width:48px">Innovative Research</div>
    <div class="pill" style="left:118px;top:26px;width:48px">Capacity Development</div>
    <div class="pill" style="left:8px;top:72px;width:48px">Knowledge Solutions</div>
    <div class="pill" style="left:118px;top:72px;width:48px">Publications &amp; Information Services</div>
  </div>
  <div class="meta"><span>10</span><span class="star">★</span></div>
</section>

<!-- 11 Section: Innovative Research -->
<section class="thumb" style="left:814px;top:149px">
  <div class="slide">
    <div class="photo" role="img" aria-label="Photograph of a hand using a tablet with charts" style="left:70px;top:0;width:103px;height:98px;background:linear-gradient(150deg,#e8eaec,#b7bcc2);clip-path:polygon(25% 0,100% 0,100% 100%,0 100%)"></div>
    <svg class="abs" style="left:0;top:0" width="173" height="98"><polygon points="0,0 95,0 75,98 0,98" fill="#1fa64a"/><polygon points="0,98 40,60 60,98" fill="#0f6b34"/><polygon points="30,10 38,3 42,13" fill="#0f6b34"/></svg>
    <div class="section-box">INNOVATIVE<br>RESEARCH</div>
  </div>
  <div class="meta"><span>11</span><span class="star">★</span></div>
</section>

<!-- 12 Innovative research -->
<section class="thumb" style="left:1014px;top:149px">
  <div class="slide">
    <div class="photo" role="img" aria-label="Dark photograph of an office desk" style="left:0;top:0;width:173px;height:22px;background:linear-gradient(90deg,#2e3034,#55585d)"></div>
    <div class="title" style="color:#fff">Innovative research</div>
    <div class="photo" role="img" aria-label="Photograph of a hand touching a glowing screen" style="left:10px;top:20px;width:40px;height:30px;background:linear-gradient(135deg,#9fb3c8,#d9e3ec)"></div>
    <div class="photo" role="img" aria-label="Photograph of documents and charts on a desk" style="left:66px;top:20px;width:40px;height:30px;background:linear-gradient(135deg,#c4cdd4,#eef1f3)"></div>
    <div class="photo" role="img" aria-label="Photograph of a researcher working at night" style="left:122px;top:20px;width:40px;height:30px;background:linear-gradient(135deg,#1d2632,#4a5a70)"></div>
    <div class="abs tiny" style="left:8px;top:55px;width:46px;text-align:center;color:var(--muted)">We are a pioneer in conducting, promoting and encouraging research in economics, banking and finance.</div>
    <div class="abs tiny" style="left:64px;top:55px;width:46px;text-align:center;color:var(--muted)">Our research seeks to identify challenges of economic development facing member countries.</div>
    <div class="abs tiny" style="left:120px;top:55px;width:46px;text-align:center;color:var(--muted)">Our research formulates solutions and strategies to address the challenges faced.</div>
    <div class="abs" style="left:8px;top:90px;width:26px;height:3px;background:var(--gold-light)"></div>
    <div class="foot-badge"></div>
  </div>
  <div class="meta"><span>12</span><span class="star">★</span></div>
</section>

<!-- 13 Research products -->
<section class="thumb" style="left:14px;top:288px">
  <div class="slide light">
    <div class="title">Research products &amp; services</div>
    <svg class="abs" style="left:0;top:24px" width="173" height="40" font-family="Open Sans,sans-serif">
      <g>
        <polygon points="28,2 40,8 40,22 28,28 16,22 16,8" fill="#1fa64a"/><polygon points="28,2 40,8 28,14 16,8" fill="#0f6b34"/>
        <polygon points="68,2 80,8 80,22 68,28 56,22 56,8" fill="#1fa64a"/><polygon points="68,2 80,8 68,14 56,8" fill="#0f6b34"/>
        <polygon points="108,2 120,8 120,22 108,28 96,22 96,8" fill="#1fa64a"/><polygon points="108,2 120,8 108,14 96,8" fill="#0f6b34"/>
        <polygon points="148,2 160,8 160,22 148,28 136,22 136,8" fill="#1fa64a"/><polygon points="148,2 160,8 148,14 136,8" fill="#0f6b34"/>
      </g>
      <g fill="#fff" font-size="3.4" text-anchor="middle"><text x="28" y="11">01</text><text x="68" y="11">02</text><text x="108" y="11">03</text><text x="148" y="11">04</text></g>
    </svg>
    <div class="abs tiny" style="left:14px;top:58px;width:28px;text-align:center;color:var(--muted)">In-house and Joint Research</div>
    <div class="abs tiny" style="left:54px;top:58px;width:28px;text-align:center;color:var(--muted)">Research products (journals, books, reports)</div>
    <div class="abs tiny" style="left:94px;top:58px;width:28px;text-align:center;color:var(--muted)">Research Events (conferences, workshops)</div>
    <div class="abs tiny" style="left:134px;top:58px;width:28px;text-align:center;color:var(--muted)">NDB Prize</div>
    <div class="abs" style="left:8px;top:90px;width:26px;height:3px;background:var(--gold-light)"></div>
    <div class="foot-badge"></div>
  </div>
  <div class="meta"><span>13</span><span class="star">★</span></div>
</section>

<!-- 14 Research areas -->
<section class="thumb" style="left:214px;top:288px">
  <div class="slide dark" role="img" aria-label="Dark photograph of a meeting room" style="background:linear-gradient(135deg,#3a3c40,#1f2024)">
    <div class="title">Research areas</div>
    <div class="tile" style="left:8px;top:18px;width:34px;height:16px">Smart Economy</div>
    <div class="tile" style="left:45px;top:18px;width:34px;height:16px">Islamic Fintech</div>
    <div class="tile" style="left:82px;top:18px;width:34px;height:16px">Zakat Management</div>
    <div class="tile" style="left:119px;top:18px;width:34px;height:16px">Management and Development of Awqaf</div>
    <div class="tile" style="left:8px;top:37px;width:34px;height:16px">Islamic Microfinance</div>
    <div class="tile" style="left:45px;top:37px;width:34px;height:16px">Islamic Financial Inclusion</div>
    <div class="tile" style="left:82px;top:37px;width:34px;height:16px">Islamic Banking</div>
    <div class="tile" style="left:119px;top:37px;width:34px;height:16px">Sukuk and Islamic Capital Market</div>
    <div class="tile" style="left:8px;top:56px;width:34px;height:16px">Shariah Structuring</div>
    <div class="tile" style="left:45px;top:56px;width:34px;height:20px">Comprehensive Human Development Based on Maqasid Al Shariah</div>
    <div class="foot-badge"></div>
  </div>
  <div class="meta"><span>14</span><span class="star">★</span></div>
</section>

<!-- 15 Section: Capacity Development -->
<section class="thumb" style="left:414px;top:288px">
  <div class="slide">
    <div class="photo" role="img" aria-label="Photograph of a hand holding a network of people icons" style="left:70px;top:0;width:103px;height:98px;background:linear-gradient(150deg,#0e2a4a,#2f6fa8 60%,#7fb3dd);clip-path:polygon(25% 0,100% 0,100% 100%,0 100%)"></div>
    <svg class="abs" style="left:0;top:0" width="173" height="98"><polygon points="0,0 95,0 75,98 0,98" fill="#1fa64a"/><polygon points="0,98 40,60 60,98" fill="#0f6b34"/><polygon points="30,10 38,3 42,13" fill="#0f6b34"/></svg>
    <div class="section-box">CAPACITY<br>DEVELOPMENT</div>
  </div>
  <div class="meta"><span>15</span><span class="star">★</span></div>
</section>

<!-- 16 Programs -->
<section class="thumb" style="left:614px;top:288px">
  <div class="slide light">
    <div class="title">Programs</div>
    <div class="photo" role="img" aria-label="Photograph of a training session" style="left:8px;top:20px;width:14px;height:12px;background:linear-gradient(135deg,#6b6e73,#a7abb0)"></div>
    <div class="photo" role="img" aria-label="Photograph of a conference hall" style="left:8px;top:42px;width:14px;height:12px;background:linear-gradient(135deg,#7b6450,#c2a98a)"></div>
    <div class="photo" role="img" aria-label="Photograph of a leaders' workshop" style="left:8px;top:64px;width:14px;height:12px;background:linear-gradient(135deg,#8a5a2c,#d99a4e)"></div>
    <div class="abs tiny" style="left:26px;top:23px;width:40px;color:var(--muted)">Programs for Private Sector</div>
    <div class="abs tiny" style="left:26px;top:45px;width:40px;color:var(--muted)">Programs for NDB Member Countries</div>
    <div class="abs tiny" style="left:26px;top:67px;width:40px;color:var(--muted)">Knowledge Leaders Program</div>
    <div class="abs" style="left:92px;top:21px;width:12px;height:10px;border-radius:2px;background:#c9bf9a"></div>
    <div class="abs" style="left:92px;top:43px;width:12px;height:10px;font-size:4px;font-weight:700;color:var(--ink)">Lumora</div>
    <div class="abs" style="left:93px;top:64px;width:11px;height:11px;border-radius:50%;background:#9cc9e0"></div>
    <div class="abs tiny" style="left:110px;top:23px;color:var(--muted)">Training<br>Packages</div>
    <div class="abs tiny" style="left:110px;top:45px;color:var(--muted)">Online Learning<br>Programs</div>
    <div class="abs tiny" style="left:110px;top:67px;color:var(--muted)">Certification<br>Program</div>
    <svg class="abs" style="left:8px;top:36px" width="160" height="30" stroke="#ddd" stroke-width=".4"><line x1="0" y1="1" x2="160" y2="1"/><line x1="0" y1="23" x2="160" y2="23"/></svg>
    <div class="abs" style="left:8px;top:90px;width:26px;height:3px;background:var(--gold-light)"></div>
    <div class="foot-badge"></div>
  </div>
  <div class="meta"><span>16</span><span class="star">★</span></div>
</section>

<!-- 17 Topics -->
<section class="thumb" style="left:814px;top:288px">
  <div class="slide dark" role="img" aria-label="Muted photograph of people working at a table" style="background:linear-gradient(135deg,#3b3c3f,#77797c 60%,#a9aaac)">
    <div class="title">Topics</div>
    <div class="tile" style="left:8px;top:20px;width:42px;height:18px">01 Principles of Islamic Economics, Banking &amp; Finance</div>
    <div class="tile" style="left:60px;top:20px;width:42px;height:18px">04 Shariah Supervision and Auditing of Islamic Institutions</div>
    <div class="tile" style="left:112px;top:20px;width:42px;height:14px">07 Corporate Governance for Islamic Institutions</div>
    <div class="tile" style="left:8px;top:44px;width:42px;height:18px">02 Regulation and Supervision of Islamic Banks</div>
    <div class="tile" style="left:60px;top:44px;width:42px;height:14px">05 Sukuk: Shariah and Operational Aspects</div>
    <div class="tile" style="left:8px;top:68px;width:42px;height:14px">03 Risk Management in Islamic Institutions</div>
    <div class="tile" style="left:60px;top:68px;width:42px;height:14px">06 Shariah Standards for Islamic Institutions</div>
  </div>
  <div class="meta"><span>17</span><span class="star">★</span></div>
</section>

<!-- 18 Topics -->
<section class="thumb" style="left:1014px;top:288px">
  <div class="slide dark" role="img" aria-label="Muted photograph of people working at a table" style="background:linear-gradient(135deg,#3b3c3f,#77797c 60%,#a9aaac)">
    <div class="title">Topics</div>
    <div class="tile" style="left:8px;top:20px;width:42px;height:18px">08 Liquidity Management in Islamic Financial Institutions</div>
    <div class="tile" style="left:60px;top:20px;width:42px;height:14px">11 Management of Awqaf for Poverty Alleviation</div>
    <div class="tile" style="left:112px;top:20px;width:42px;height:18px">14 Public-Private Partnership (PPP) for Infrastructure Projects</div>
    <div class="tile" style="left:8px;top:44px;width:42px;height:14px">09 Islamic Capital Markets</div>
    <div class="tile" style="left:60px;top:44px;width:42px;height:14px">12 Islamic Microfinance for Poverty Alleviation</div>
    <div class="tile" style="left:8px;top:68px;width:42px;height:14px">10 Management of Zakah for Poverty Alleviation</div>
    <div class="tile" style="left:60px;top:68px;width:42px;height:14px">13 Preparing Small and Medium Enterprises</div>
  </div>
  <div class="meta"><span>18</span><span class="star">★</span></div>
</section>

<!-- 19 Online learning programs -->
<section class="thumb" style="left:14px;top:427px">
  <div class="slide light">
    <div class="title">Online learning programs</div>
    <div class="abs" style="left:12px;top:17px;width:30px;height:24px;background:#efe8d2;display:flex;flex-direction:column;align-items:center;justify-content:center">
      <span style="font-size:5px;font-weight:700;color:var(--ink)">Lumora</span>
      <span style="font-size:2.6px;color:var(--green);text-decoration:underline">lumora.org/kvob</span>
    </div>
    <div class="abs" style="left:12px;top:44px;width:30px;height:32px;background:#efe8d2;text-align:center;padding-top:3px">
      <div style="font-size:6px;font-weight:700">45000</div>
      <div style="font-size:2.6px;color:var(--muted)">Beneficiaries</div>
      <div style="font-size:6px;font-weight:700;margin-top:2px">8 <span style="font-size:2.6px;font-weight:400;color:var(--muted)">Courses</span></div>
    </div>
    <div class="abs" style="left:50px;top:16px;width:90px;height:60px;border-radius:5px;background:#3a3b3e;padding:5px 7px">
      <div style="display:grid;grid-template-columns:repeat(3,1fr);gap:2px;background:#fff;height:100%;padding:3px">
        <div role="img" aria-label="Course preview image" style="background:#8aa7bf"></div>
        <div role="img" aria-label="Course preview image" style="background:#c79d68"></div>
        <div role="img" aria-label="Course preview image" style="background:#7d9a7a"></div>
        <div role="img" aria-label="Course preview image" style="background:#a9927f"></div>
        <div role="img" aria-label="Course preview image" style="background:#6f87a3"></div>
        <div role="img" aria-label="Course preview image" style="background:#b8b08a"></div>
      </div>
    </div>
    <div class="foot-badge"></div>
  </div>
  <div class="meta"><span>19</span><span class="star">★</span></div>
</section>

<!-- 20 Section: Knowledge Solutions -->
<section class="thumb" style="left:214px;top:427px">
  <div class="slide">
    <div class="photo" role="img" aria-label="Photograph of a businessman holding a tablet" style="left:70px;top:0;width:103px;height:98px;background:linear-gradient(150deg,#2b2d31,#8d9096 60%,#d9dadc);clip-path:polygon(25% 0,100% 0,100% 100%,0 100%)"></div>
    <svg class="abs" style="left:0;top:0" width="173" height="98"><polygon points="0,0 95,0 75,98 0,98" fill="#1fa64a"/><polygon points="0,98 40,60 60,98" fill="#0f6b34"/><polygon points="30,10 38,3 42,13" fill="#0f6b34"/></svg>
    <div class="section-box">KNOWLEDGE<br>SOLUTIONS</div>
  </div>
  <div class="meta"><span>20</span><span class="star">★</span></div>
</section>

<!-- 21 Objectives -->
<section class="thumb" style="left:414px;top:427px">
  <div class="slide dark" role="img" aria-label="Night photograph of a city skyline" style="background:linear-gradient(180deg,#15181d,#3a4049 60%,#6a6f76)">
    <div class="title">Objectives</div>
    <div class="abs" style="left:0;top:30px;width:92px;height:50px;background:rgba(138,122,60,.85);border-radius:0 25px 25px 0;padding:5px 6px;font-size:3.2px;line-height:1.4;color:#fff">The Knowledge Solutions initiative objective is to transform critical components of the economy of member countries using fintech innovations and technologies (AI, Blockchain, IoT, etc.) to bring about value-based, inclusive and sustainable growth in line with principles of Islamic economics and finance.</div>
  </div>
  <div class="meta"><span>21</span><span class="star">★</span></div>
</section>

</main>
</body>
</html>
```